Youth organisation needs design work for awards booklet

We are from The Young Pathfinders' Corps in Singapore, and we need design work for an awards booklet for one of our most prestigious awards, the Keystone Honour. The recipients are sixteen year old teenagers. This booklet will comprise of the list of the recipients, congratulatory notes and stories from some of the recipients. This booklet will be printed for each of the recipient and his guests to keep as a remembrance. We are looking for dual or tri-colour scheme, with bronze being one of the colours.
Updates

Target Market(s)

Recipients of the Award, their parents, school Principals and teachers

Requirements
Must have
• We are looking to have around 16 designed pages, including front and back cover. Size of the booklet is:
Closed - W100mm x H210mm; Opened - W200mm x H210mm
Cover page - picture of the Award
Page 3 - programme highlights
Page 4-5 - picture of the Award and description of the Award
Page 6-7 - Testimonials
Page 8-14 - List of recipients (to be provided upon confirmation of designer)
Page 15 - blank page or acknowledgments page
Back Cover - YP Logo and contact details
(Refer to previous years' booklets for reference)

Designers can submit just the cover pages as well as 1 sample inner page to get a sense of the overall style of design during the selection round.
Nice to have
• Clean, prestigious/premium look

```html
<!DOCTYPE html>
<html lang="en">
<head>
<meta charset="utf-8">
<title>Keystone Honour Recipients</title>
<link rel="stylesheet" href="https://fonts.googleapis.com/css2?family=Montserrat:wght@500;600;700;800;900&family=Jost:wght@500&display=swap">
<style>
  :root {
    --bronze: #bd9658;
    --ink: #161616;
    --paper: #ffffff;
    --backdrop: #dcdcdc;
  }
  * { margin: 0; padding: 0; box-sizing: border-box; }
  html, body { width: 1147px; height: 1200px; overflow: hidden; background: var(--backdrop); }
  .spread { position: relative; width: 1147px; height: 1200px; }
  .page-sheet { position: absolute; left: 53px; top: 52px; width: 1043px; height: 1095px; background: var(--paper); }
  .fold-line { position: absolute; left: 573px; top: 35px; height: 1130px; border-left: 1px dashed #555; }

  .title-block { position: absolute; left: 144px; width: 340px; top: 128px; text-align: center; font-family: 'Montserrat', sans-serif; color: #000; }
  .title-kicker { font-weight: 800; font-size: 22px; letter-spacing: 2.5px; line-height: 30px; }
  .title-main { font-weight: 900; font-size: 47px; letter-spacing: 4px; line-height: 44px; }
  .title-rule { position: absolute; left: 144px; top: 210px; width: 340px; height: 2px; background: #000; }
  .intro { position: absolute; left: 106px; width: 416px; top: 244px; text-align: center; font-family: 'Montserrat', sans-serif; font-weight: 500; font-size: 15.5px; line-height: 18px; letter-spacing: 0.8px; color: var(--ink); }
  .intro strong { font-weight: 800; }

  .award-box { position: absolute; width: 416px; border: 2px solid var(--bronze); text-align: center; padding-top: 22px; }
  .col-left { left: 106px; }
  .col-right { left: 627px; }
  .company-band { position: absolute; top: -17px; left: 50%; transform: translateX(-50%); min-width: 331px; height: 31px; padding: 0 16px; background: var(--bronze); color: #fff; font-family: 'Montserrat', sans-serif; font-weight: 800; font-size: 19px; line-height: 31px; letter-spacing: 1px; white-space: nowrap; }
  .company-band.wide { min-width: 345px; }
  .unit-host { font-family: 'Montserrat', sans-serif; font-weight: 600; font-size: 15.5px; line-height: 16.6px; color: var(--bronze); letter-spacing: 0.4px; }
  .recipient-list { margin-top: 13px; font-family: 'Jost', sans-serif; font-weight: 500; font-size: 16px; line-height: 18.4px; color: var(--ink); }
  .recipient-row { display: flex; justify-content: center; gap: 12px; white-space: nowrap; }
  .recipient { display: inline-flex; align-items: center; gap: 7px; }
  .recipient::before { content: ""; width: 8px; height: 10px; background: var(--bronze); border-radius: 50% 50% 50% 50% / 60% 60% 42% 42%; }
</style>
</head>
<body>
<div class="spread">
  <div class="page-sheet"></div>
  <div class="fold-line"></div>

  <header class="title-block">
    <div class="title-kicker">KEYSTONE HONOUR</div>
    <h1 class="title-main">RECIPIENTS</h1>
  </header>
  <div class="title-rule"></div>
  <p class="intro">This year, we are proud to present the<br><strong>Keystone Honour</strong> to the following recipients:</p>

  <section class="award-box col-left" style="top:330px;height:158px">
    <h2 class="company-band">2nd SINGAPORE COMPANY</h2>
    <div class="unit-host">Harbourview School<br>Kallang Grove Methodist Church</div>
    <div class="recipient-list">
      <div class="recipient-row"><span class="recipient">SSG Tan Wei Jie Marcus</span><span class="recipient">SSG Lau Jun Hao Darren</span></div>
      <div class="recipient-row"><span class="recipient">SSG Eli Koh</span><span class="recipient">SSG Nathan Paolo Reyes</span></div>
      <div class="recipient-row"><span class="recipient">SSG Goh Yi Ming</span><span class="recipient">SSG Caleb Teo Qirui</span></div>
      <div class="recipient-row"><span class="recipient">WO Sim Kah Wei Jonathan</span></div>
    </div>
  </section>

  <section class="award-box col-left" style="top:537px;height:142px">
    <h2 class="company-band">5th SINGAPORE COMPANY</h2>
    <div class="unit-host">Seng Hock Presbyterian Secondary School<br>Bukit Tinggi Presbyterian Church</div>
    <div class="recipient-list">
      <div class="recipient-row"><span class="recipient">WO Ryan Ong</span><span class="recipient">WO Karthikeyan</span></div>
      <div class="recipient-row"><span class="recipient">WO Suresh Arvind</span><span class="recipient">WO Darius Ethan Lim</span></div>
      <div class="recipient-row"><span class="recipient">Xu Jia Le</span></div>
    </div>
  </section>

  <section class="award-box col-left" style="top:727px;height:141px">
    <h2 class="company-band">7th SINGAPORE COMPANY</h2>
    <div class="unit-host">Seng Hock Presbyterian Secondary School<br>Bukit Tinggi Presbyterian Church</div>
    <div class="recipient-list">
      <div class="recipient-row"><span class="recipient">WO Ryan Ong</span><span class="recipient">WO Karthikeyan</span></div>
      <div class="recipient-row"><span class="recipient">WO Suresh Arvind</span><span class="recipient">WO Darius Ethan Lim</span></div>
      <div class="recipient-row"><span class="recipient">Xu Jia Le</span></div>
    </div>
  </section>

  <section class="award-box col-left" style="top:916px;height:158px">
    <h2 class="company-band wide">10th SINGAPORE COMPANY</h2>
    <div class="unit-host">Harbourview School<br>Kallang Grove Methodist Church</div>
    <div class="recipient-list">
      <div class="recipient-row"><span class="recipient">SSG Tan Wei Jie Marcus</span><span class="recipient">SSG Lau Jun Hao Darren</span></div>
      <div class="recipient-row"><span class="recipient">SSG Eli Koh</span><span class="recipient">SSG Nathan Paolo Reyes</span></div>
      <div class="recipient-row"><span class="recipient">SSG Goh Yi Ming</span><span class="recipient">SSG Caleb Teo Qirui</span></div>
      <div class="recipient-row"><span class="recipient">WO Sim Kah Wei Jonathan</span></div>
    </div>
  </section>

  <section class="award-box col-right" style="top:154px;height:158px">
    <h2 class="company-band">2nd SINGAPORE COMPANY</h2>
    <div class="unit-host">Harbourview School<br>Kallang Grove Methodist Church</div>
    <div class="recipient-list">
      <div class="recipient-row"><span class="recipient">SSG Tan Wei Jie Marcus</span><span class="recipient">SSG Lau Jun Hao Darren</span></div>
      <div class="recipient-row"><span class="recipient">SSG Eli Koh</span><span class="recipient">SSG Nathan Paolo Reyes</span></div>
      <div class="recipient-row"><span class="recipient">SSG Goh Yi Ming</span><span class="recipient">SSG Caleb Teo Qirui</span></div>
      <div class="recipient-row"><span class="recipient">WO Sim Kah Wei Jonathan</span></div>
    </div>
  </section>

  <section class="award-box col-right" style="top:362px;height:141px">
    <h2 class="company-band">5th SINGAPORE COMPANY</h2>
    <div class="unit-host">Seng Hock Presbyterian Secondary School<br>Bukit Tinggi Presbyterian Church</div>
    <div class="recipient-list">
      <div class="recipient-row"><span class="recipient">WO Ryan Ong</span><span class="recipient">WO Karthikeyan</span></div>
      <div class="recipient-row"><span class="recipient">WO Suresh Arvind</span><span class="recipient">WO Darius Ethan Lim</span></div>
      <div class="recipient-row"><span class="recipient">Xu Jia Le</span></div>
    </div>
  </section>

  <section class="award-box col-right" style="top:549px;height:267px">
    <h2 class="company-band wide">121 SINGAPORE COMPANY</h2>
    <div class="unit-host">Harbourview School<br>Kallang Grove Methodist Church</div>
    <div class="recipient-list">
      <div class="recipient-row"><span class="recipient">SSG Tan Wei Jie Marcus</span><span class="recipient">SSG Lau Jun Hao Darren</span></div>
      <div class="recipient-row"><span class="recipient">SSG Eli Koh</span><span class="recipient">SSG Nathan Paolo Reyes</span></div>
      <div class="recipient-row"><span class="recipient">SSG Goh Yi Ming</span><span class="recipient">SSG Caleb Teo Qirui</span></div>
      <div class="recipient-row"><span class="recipient">WO Sim Kah Wei Jonathan</span><span class="recipient">SSG Tan Wei Jie Marcus</span></div>
      <div class="recipient-row"><span class="recipient">SSG Lau Jun Hao Darren</span><span class="recipient">SSG Eli Koh</span></div>
      <div class="recipient-row"><span class="recipient">SSG Nathan Paolo Reyes</span><span class="recipient">SSG Goh Yi Ming</span></div>
      <div class="recipient-row"><span class="recipient">SSG Caleb Teo Qirui</span><span class="recipient">WO Sim Kah Wei Jonathan</span></div>
      <div class="recipient-row"><span class="recipient">WO Ryan Ong</span><span class="recipient">WO Karthikeyan</span></div>
      <div class="recipient-row"><span class="recipient">WO Suresh Arvind</span><span class="recipient">WO Darius Ethan Lim</span></div>
      <div class="recipient-row"><span class="recipient">Xu Jia Le</span></div>
    </div>
  </section>

  <section class="award-box col-right" style="top:858px;height:216px">
    <h2 class="company-band wide">121 SINGAPORE COMPANY</h2>
    <div class="unit-host">Harbourview School<br>Kallang Grove Methodist Church</div>
    <div class="recipient-list">
      <div class="recipient-row"><span class="recipient">SSG Tan Wei Jie Marcus</span><span class="recipient">SSG Lau Jun Hao Darren</span></div>
      <div class="recipient-row"><span class="recipient">SSG Eli Koh</span><span class="recipient">SSG Nathan Paolo Reyes</span></div>
      <div class="recipient-row"><span class="recipient">SSG Goh Yi Ming</span><span class="recipient">SSG Caleb Teo Qirui</span></div>
      <div class="recipient-row"><span class="recipient">WO Sim Kah Wei Jonathan</span><span class="recipient">SSG Tan Wei Jie Marcus</span></div>
      <div class="recipient-row"><span class="recipient">SSG Lau Jun Hao Darren</span><span class="recipient">SSG Eli Koh</span></div>
      <div class="recipient-row"><span class="recipient">SSG Nathan Paolo Reyes</span><span class="recipient">SSG Goh Yi Ming</span></div>
      <div class="recipient-row"><span class="recipient">SSG Caleb Teo Qirui</span><span class="recipient">WO Sim Kah Wei Jonathan</span></div>
    </div>
  </section>
</div>
</body>
</html>
```